Anzeigengestaltung für Finanzierungsberatung und Bankenkommunikation
Zielgruppe
Beratung für mittelständische Unternehmen, Schwerpunkt Finanzierungsberatung und Bankenkommunikation
Motto: Mit Kreditgebern auf Augenhöhe kommunizieren
Beratungsschwerpunkte:
- Mittelstandsfinanzierung
- Baufinanzierung
- Existenzgründerfinanzierung
Aufgabenstellung
Mit Kreditgebern auf Augenhöhe kommunizieren als Leitsatz
persönliche Note sollte rüber kommen, ich mache Werbung in einer Region, wo mich die Zielgruppe noch persönlich aus der Bank kennt. Daher ist mir eine Anzeige mit Foto wichtig.
Anzeigenformat
Breite 90mm
Höhe 60 mm

```html
<!DOCTYPE html>
<html lang="de">
<head>
<meta charset="utf-8">
<title>KreditKlar – Anzeige</title>
<link rel="stylesheet" href="https://fonts.googleapis.com/css2?family=Arimo:wght@400;700&family=Nunito+Sans:wght@400&display=swap">
<style>
  :root {
    --purple: #8e2d8f;
    --slate: #5f6772;
    --text-grey: #58606b;
    --ink: #111111;
    --paper: #ffffff;
    --photo-light: #f7f6f5;
    --photo-mid: #e9e6e3;
  }
  html, body {
    margin: 0;
    width: 1200px;
    height: 990px;
    overflow: hidden;
    background: var(--paper);
  }
  .ad {
    position: absolute;
    left: 56px;
    top: 132px;
    width: 1084px;
    height: 723px;
    background: var(--paper);
    border: 1.5px solid var(--purple);
    box-sizing: border-box;
    box-shadow: 3px 5px 6px rgba(0,0,0,0.35);
    overflow: hidden;
    font-family: "Arimo", Arial, sans-serif;
  }
  .portrait {
    position: absolute;
    left: 50px;
    top: 10px;
    width: 360px;
    height: 642px;
    background: linear-gradient(160deg, var(--photo-light) 0%, var(--photo-mid) 70%, var(--photo-light) 100%);
    -webkit-mask-image: linear-gradient(90deg, #000 0%, #000 75%, transparent 100%);
    mask-image: linear-gradient(90deg, #000 0%, #000 75%, transparent 100%);
  }
  .swoosh {
    position: absolute;
    inset: 0;
  }
  .brand {
    position: absolute;
    left: 458px;
    top: 22px;
    margin: 0;
    font-family: "Nunito Sans", sans-serif;
    font-weight: 400;
    font-size: 92px;
    letter-spacing: 1px;
    line-height: 1;
    color: var(--purple);
  }
  .brand-tagline {
    position: absolute;
    left: 520px;
    top: 124px;
    margin: 0;
    font-size: 11px;
    color: #ececec;
    letter-spacing: 2px;
  }
  .motto {
    position: absolute;
    left: 461px;
    top: 160px;
    margin: 0;
    font-size: 34px;
    line-height: 42px;
    font-weight: 700;
    color: var(--text-grey);
  }
  .services {
    position: absolute;
    left: 420px;
    top: 256px;
    margin: 0;
    padding: 0;
    list-style: none;
    font-size: 30px;
    line-height: 38px;
    color: var(--ink);
  }
  .services li {
    position: relative;
    padding-left: 41px;
  }
  .services .tick {
    position: absolute;
    left: 0;
    top: 0;
    width: 28px;
    height: 34px;
  }
  .services .tick path {
    fill: none;
    stroke: var(--purple);
    stroke-width: 4.5;
    stroke-linecap: round;
    stroke-linejoin: round;
  }
  .contact {
    position: absolute;
    left: 461px;
    top: 456px;
    margin: 0;
    font-style: normal;
    font-size: 30px;
    line-height: 36px;
    color: var(--ink);
  }
  .contact strong { font-weight: 700; }
  .footer {
    position: absolute;
    left: 0;
    right: 0;
    top: 670px;
    margin: 0;
    text-align: center;
    font-size: 34px;
    font-weight: 700;
    color: var(--paper);
    white-space: nowrap;
  }
  .footer .divider {
    display: inline-block;
    width: 2px;
    height: 40px;
    background: var(--paper);
    vertical-align: -7px;
    margin: 0 12px;
  }
</style>
</head>
<body>
  <div class="ad">
    <div class="portrait" role="img" aria-label="Porträtfoto der Beraterin in weißem Shirt vor hellem Hintergrund"></div>

    <svg class="swoosh" width="1084" height="723" viewBox="0 0 1084 723" aria-hidden="true">
      <path d="M0,645 Q280,615 540,570 L540,723 L0,723 Z" fill="#ffffff"/>
      <path d="M0,669 Q700,610 1084,504 L1084,723 L0,723 Z" fill="var(--slate)"/>
    </svg>

    <h1 class="brand">KreditKlar</h1>
    <p class="brand-tagline">mit Kreditgebern auf Augenhöhe kommunizieren</p>

    <h2 class="motto">Mit Kreditgebern auf<br>Augenhöhe kommunizieren</h2>

    <ul class="services">
      <li><svg class="tick" viewBox="0 0 28 34" aria-hidden="true"><path d="M3,19 L11,30 L25,3"/></svg>Mittelstandsfinanzierung</li>
      <li><svg class="tick" viewBox="0 0 28 34" aria-hidden="true"><path d="M3,19 L11,30 L25,3"/></svg>Existenzgründerberatung</li>
      <li><svg class="tick" viewBox="0 0 28 34" aria-hidden="true"><path d="M3,19 L11,30 L25,3"/></svg>Baufinanzierung für Selbständige<br>und Privatpersonen</li>
    </ul>

    <address class="contact">
      Tel.: <strong>0151-2048731</strong><br>
      info@kreditklar.de<br>
      www.kreditklar.de
    </address>

    <p class="footer">Lena-Marie Hofbauer<span class="divider"></span>Lindenweg 4<span class="divider"></span>31134 Hildesheim</p>
  </div>
</body>
</html>
```